front and back labels on a single sheet.

Vodka label design
Vodka is a colourless liquor. This vodka is tasteless and with no flavour.

FRONT LABEL
"GRISE STAMP" is the brand name . it should be as big as possible.
below that " Only vodka made from sustainable means"
Remaining details to be copied from attached file.
Back Label
Details attached.

Colors
00AB8E
00BBA5
67D7C9
C6EFE9
E9F9F6

```html
<!DOCTYPE html>
<html lang="en">
<head>
<meta charset="UTF-8">
<title>Grise Stamp Vodka – Front and Back Labels</title>
<link rel="stylesheet" href="https://fonts.googleapis.com/css2?family=Bebas+Neue&family=Montserrat:wght@300;500;700;800&display=swap">
<style>
  :root {
    --sheet: #ece6d6;
    --label-white: #ffffff;
    --label-mist: #eeeeef;
    --gold-deep: #b8892a;
    --gold-mid: #d6ab45;
    --gold-light: #f3d98a;
    --gold-pale: #fbeab0;
    --ink: #2b2b2b;
    --ink-soft: #6a6a6a;
    --rule: #9b9b9b;
    --brand-green: #2e8b2e;
    --warning-red: #d9202a;
  }
  * { box-sizing: border-box; margin: 0; padding: 0; }
  html, body { width: 1033px; height: 1200px; overflow: hidden; }
  body {
    background: var(--sheet);
    font-family: "Montserrat", sans-serif;
    position: relative;
  }
  .label {
    position: absolute;
    top: 280px;
    width: 442px;
    height: 640px;
    overflow: hidden;
    background: var(--label-white);
    box-shadow: 0 6px 24px rgba(0,0,0,0.12);
  }
  .label--front { left: 50px; }
  .label--back { left: 541px; }
  .label__ground { position: absolute; inset: 0; width: 100%; height: 100%; }
  .label__texture {
    position: absolute; left: 0; top: 0; width: 100%; height: 110px;
    background: linear-gradient(180deg, #dcdcde 0%, #f1f1f2 60%, rgba(255,255,255,0) 100%);
  }

  /* Front */
  .brand {
    position: absolute; top: 40px; left: 0; width: 100%;
    text-align: center;
  }
  .brand__name {
    display: inline-flex; align-items: center; gap: 7px;
    font-weight: 700; font-size: 15px; letter-spacing: 0.5px;
    color: var(--brand-green);
  }
  .brand__dot { width: 12px; height: 12px; border-radius: 50%; background: var(--brand-green); }
  .brand__tagline {
    margin-top: 3px; font-size: 5px; font-weight: 500; letter-spacing: 0.3px; color: var(--ink-soft);
  }
  .title-card {
    position: absolute; left: 38px; top: 140px; width: 366px; height: 360px;
    background: var(--label-white);
    text-align: center;
  }
  .title-card__name {
    margin-top: 6px;
    font-family: "Bebas Neue", sans-serif;
    font-size: 172px; line-height: 0.86; letter-spacing: 2px;
    background: linear-gradient(100deg, var(--gold-deep) 0%, var(--gold-mid) 30%, var(--gold-pale) 55%, var(--gold-mid) 75%, var(--gold-deep) 100%);
    -webkit-background-clip: text; background-clip: text; color: transparent;
  }
  .title-card__claim {
    position: absolute; left: 0; bottom: 12px; width: 100%;
    font-family: "Bebas Neue", sans-serif; font-size: 23px; letter-spacing: 0.3px;
    color: var(--gold-deep);
  }
  .grade {
    position: absolute; top: 532px; left: 0; width: 100%;
    display: flex; align-items: center; gap: 14px;
    font-family: "Bebas Neue", sans-serif; font-size: 21px; letter-spacing: 2px; color: var(--label-white);
  }
  .grade::before, .grade::after { content: ""; flex: 1; height: 1px; background: rgba(255,255,255,0.8); }
  .specs {
    position: absolute; left: 26px; right: 22px; top: 578px;
    display: flex; justify-content: space-between;
    font-family: "Bebas Neue", sans-serif; font-size: 36px; letter-spacing: 2px; color: var(--label-white);
  }

  /* Back */
  .story {
    position: absolute; top: 112px; left: 30px; right: 30px;
    text-align: center; font-size: 11.3px; font-weight: 500; line-height: 1.65; color: var(--ink);
  }
  .rule { position: absolute; left: 42px; right: 42px; height: 1px; background: var(--rule); }
  .rule--upper { top: 218px; }
  .rule--lower { top: 320px; }
  .notices { position: absolute; top: 232px; left: 42px; right: 36px; height: 60px; display: flex; align-items: center; gap: 16px; }
  .pregnancy {
    position: relative; width: 236px; height: 30px;
    border: 1px solid var(--warning-red); border-radius: 5px;
    padding-left: 38px; padding-top: 3px;
  }
  .pregnancy__icon { position: absolute; left: -2px; top: -4px; width: 34px; height: 34px; }
  .pregnancy__head { font-size: 7.5px; font-weight: 800; letter-spacing: 0.6px; color: var(--warning-red); }
  .pregnancy__text { font-size: 7px; line-height: 1.15; color: var(--ink); }
  .std-drink { width: 30px; height: 34px; }
  .recycle { width: 30px; text-align: center; font-size: 5px; font-weight: 700; margin-left: 10px; }
  .recycle svg { width: 26px; height: 26px; display: block; margin: 0 auto 1px; }
  .details { position: absolute; top: 332px; left: 42px; right: 30px; display: flex; }
  .details__col { font-size: 8.2px; font-weight: 300; line-height: 1.55; color: var(--ink); }
  .details__col--serve { width: 160px; padding-top: 2px; }
  .details__col--maker { padding-left: 20px; border-left: 1px solid var(--rule); margin-left: 8px; height: 88px; }
  .details__contact { margin-top: 4px; font-size: 5.5px; font-weight: 700; line-height: 1.4; }
  .details__origin { margin-top: 6px; font-weight: 500; }
  .source-band {
    position: absolute; top: 433px; left: 0; width: 100%; height: 38px;
    background: linear-gradient(90deg, var(--gold-deep) 0%, var(--gold-mid) 45%, var(--gold-light) 80%, var(--gold-mid) 100%);
    text-align: center; line-height: 38px;
    font-weight: 800; font-size: 23px; letter-spacing: 0.5px; color: var(--label-white);
  }
  .founder-portrait {
    position: absolute; left: 140px; top: 500px; width: 162px; height: 140px;
    background: linear-gradient(180deg, #e8e8e8 0%, #cfcfcf 100%);
  }
</style>
</head>
<body>

  <section class="label label--front" aria-label="Front label">
    <svg class="label__ground" viewBox="0 0 442 640" preserveAspectRatio="none" aria-hidden="true">
      <defs>
        <linearGradient id="frontGold" x1="0" y1="1" x2="1" y2="0">
          <stop offset="0" stop-color="#c1952f"/>
          <stop offset="0.45" stop-color="#dcb454"/>
          <stop offset="0.8" stop-color="#f1d27a"/>
          <stop offset="1" stop-color="#e0b64e"/>
        </linearGradient>
      </defs>
      <rect width="442" height="640" fill="#f4f4f5"/>
      <polygon points="0,640 0,335 442,40 442,640" fill="url(#frontGold)"/>
      <polygon points="0,640 0,470 442,300 442,640" fill="#c9a040" opacity="0.55"/>
      <polygon points="160,640 442,430 442,640" fill="#e2b950" opacity="0.6"/>
    </svg>
    <div class="label__texture" role="img" aria-label="Soft dotted halftone texture across the top of the label"></div>

    <div class="brand">
      <div class="brand__name"><span class="brand__dot"></span>VERDANT STILL</div>
      <div class="brand__tagline">SPIRITS CRAFTED WITH GENTLE NATURAL HERBS</div>
    </div>

    <div class="title-card">
      <h1 class="title-card__name">GRISE<br>STAMP</h1>
      <p class="title-card__claim">Only vodka made from sustainable means</p>
    </div>

    <p class="grade">Premium quality vodka</p>
    <div class="specs"><span>50%</span><span>750ml</span></div>
  </section>

  <section class="label label--back" aria-label="Back label">
    <svg class="label__ground" viewBox="0 0 442 640" preserveAspectRatio="none" aria-hidden="true">
      <defs>
        <linearGradient id="backGold" x1="0" y1="1" x2="1" y2="0">
          <stop offset="0" stop-color="#c1952f"/>
          <stop offset="0.5" stop-color="#e7c462"/>
          <stop offset="1" stop-color="#d6a942"/>
        </linearGradient>
      </defs>
      <rect width="442" height="640" fill="#f0f0f1"/>
      <polygon points="0,640 0,620 442,340 442,640" fill="url(#backGold)"/>
      <polygon points="230,640 442,500 442,640" fill="#d2a43f" opacity="0.6"/>
    </svg>
    <div class="label__texture" role="img" aria-label="Soft dotted halftone texture across the top of the label"></div>

    <p class="story">THE ONLY VODKA IN THE WHOLE WORLD WHICH HAS UNIQUE 5 SPICES, AND DISTILLED 3+1 TIMES. IN ADDITION THIS IS THE ONLY VODKA MADE FROM NATURAL RAINWATER &amp; SOLAR POWER, THUS MAKING IT THE ONLY VODKA THAT IS SUSTAINABLY MANUFACTURED.</p>

    <div class="rule rule--upper"></div>

    <div class="notices">
      <div class="pregnancy">
        <svg class="pregnancy__icon" viewBox="0 0 34 34" aria-hidden="true">
          <circle cx="17" cy="17" r="14" fill="#fff" stroke="var(--warning-red)" stroke-width="3.5"/>
          <line x1="7" y1="7" x2="27" y2="27" stroke="var(--warning-red)" stroke-width="3.5"/>
        </svg>
        <div class="pregnancy__head">PREGNANCY WARNING</div>
        <div class="pregnancy__text">Alcohol can cause lifelong<br>harm to your baby</div>
      </div>
      <svg class="std-drink" viewBox="0 0 30 34" aria-label="Approximately 27 standard drinks">
        <polygon points="1,1 29,1 25,33 5,33" fill="#fff" stroke="#222" stroke-width="1.5"/>
        <rect x="6" y="10" width="18" height="17" fill="#222"/>
        <text x="15" y="7" font-size="4" font-weight="700" text-anchor="middle" font-family="Montserrat, sans-serif">STANDARD</text>
        <text x="15" y="24" font-size="14" font-weight="800" fill="#fff" text-anchor="middle" font-family="Montserrat, sans-serif">27</text>
        <text x="15" y="31.5" font-size="3.6" font-weight="700" text-anchor="middle" font-family="Montserrat, sans-serif">APPROX</text>
      </svg>
      <div class="recycle">
        <svg viewBox="0 0 26 26" aria-hidden="true">
          <path d="M13 3 L21 17 M19 22 L7 22 M5 17 L11 6" fill="none" stroke="#222" stroke-width="2.4"/>
          <path d="M22 13 L21 18 L17 16 M10 19 L7 22 L10 25 M9 4 L12 5 L13 9" fill="none" stroke="#222" stroke-width="1.8"/>
        </svg>
        GLASS
      </div>
    </div>

    <div class="rule rule--lower"></div>

    <div class="details">
      <div class="details__col details__col--serve">
        THIS VODKA HAS TO BE TAKEN CHILLED WITH ICE CUBES. MAKING COCKTAILS WITH LIME AND ORANGE IS A WONDERFUL EXPERIENCE.
        <div class="details__contact">CONTACT AT:<br>HELLO@VERDANTSTILL.COM.AU</div>
      </div>
      <div class="details__col details__col--maker">
        FERMENTED AND DISTILLED BY:<br>ELWIN R. MARLOWE<br>AT VERDANT STILL PVT LTD
        <div class="details__origin">MADE IN: WILLOWMERE,<br>VICTORIA, AUSTRALIA</div>
      </div>
    </div>

    <div class="source-band">MADE FROM SUGARCANE</div>

    <div class="founder-portrait" role="img" aria-label="Pencil-sketch portrait of the distiller"></div>
  </section>

</body>
</html>
```